Consulting company needs Business Cards - rough concept provided

I'm looking for someone to take our business card idea and make is slick and polished - to communicate our high-end, sophisticated, serious consulting business. We have a rough layout we did in-house. We are open to ideas on repo-ing elements, adjusting sizes, typefaces etc... within the general concept we've already come up with. We want it to be super-clean and sophisticated. We want to keep the white backgrounds, and blue brand colors. Our goal is to print with painted blue edges on thick cardstock. Thank you!!

```html
<!DOCTYPE html>
<html lang="en">
<head>
<meta charset="utf-8">
<title>Northlark Business Cards</title>
<link rel="stylesheet" href="https://fonts.googleapis.com/css2?family=Montserrat:wght@300;400;500;600;800&display=swap">
<style>
  :root {
    --backdrop: #eceded;
    --card-white: #fbfbfa;
    --brand-blue: #1d9ad8;
    --blue-tint: #35a9e2;
    --ink: #111111;
    --ink-soft: #3a3a3a;
    --deboss: #ececeb;
    --white: #ffffff;
  }
  * { margin: 0; padding: 0; box-sizing: border-box; }
  html, body {
    width: 1200px;
    height: 1000px;
    overflow: hidden;
    background: var(--backdrop);
    font-family: "Montserrat", sans-serif;
  }
  .canvas {
    position: relative;
    width: 1200px;
    height: 1000px;
  }
  .card {
    position: absolute;
    width: 560px;
    height: 320px;
    overflow: hidden;
    border-bottom: 6px solid var(--brand-blue);
    box-shadow: 0 10px 24px rgba(0, 0, 0, 0.12);
  }

  /* Front */
  .card-front {
    left: 90px;
    top: 120px;
    background: var(--card-white);
  }
  .front-watermark {
    position: absolute;
    left: 34px;
    top: 26px;
    font-weight: 800;
    font-size: 40px;
    letter-spacing: 1px;
    color: var(--deboss);
  }
  .holder {
    position: absolute;
    left: 34px;
    top: 132px;
  }
  .holder-name {
    font-weight: 600;
    font-size: 29px;
    color: var(--ink);
    letter-spacing: 0.2px;
  }
  .holder-role {
    margin-top: 2px;
    font-weight: 300;
    font-size: 17px;
    letter-spacing: 1.2px;
    color: var(--ink-soft);
  }
  .contact {
    position: absolute;
    right: 34px;
    top: 100px;
    text-align: right;
    font-weight: 400;
    font-size: 12px;
    line-height: 1.5;
    letter-spacing: 0.5px;
    color: var(--ink);
  }
  .contact .gap { margin-top: 8px; }
  .front-logo {
    position: absolute;
    right: 34px;
    bottom: 36px;
    font-weight: 500;
    font-size: 24px;
    letter-spacing: 1px;
    color: var(--brand-blue);
  }

  /* Back */
  .card-back {
    left: 550px;
    top: 560px;
    background: var(--brand-blue);
    border-bottom-color: #1787bf;
  }
  .mission {
    position: absolute;
    left: 40px;
    right: 100px;
    top: 50%;
    transform: translateY(-50%);
    text-align: center;
    font-weight: 400;
    font-size: 18px;
    line-height: 1.3;
    letter-spacing: 1px;
    color: var(--white);
  }
  .back-watermark {
    position: absolute;
    right: -100px;
    top: 136px;
    width: 300px;
    text-align: center;
    transform: rotate(90deg);
    font-weight: 800;
    font-size: 36px;
    letter-spacing: 1px;
    color: var(--blue-tint);
  }
</style>
</head>
<body>
<main class="canvas">
  <section class="card card-front" aria-label="Business card front">
    <div class="front-watermark" aria-hidden="true">NORTHLARK</div>
    <div class="holder">
      <p class="holder-name">Dana Whitford</p>
      <p class="holder-role">Brand Consultant</p>
    </div>
    <address class="contact" style="font-style: normal;">
      <p>4820 Harbor Lane, Ste 210</p>
      <p>Lakeview, CA 90512</p>
      <p class="gap">(555) 014 2290</p>
      <p>dana@northlark.com</p>
    </address>
    <div class="front-logo">NORTHLARK</div>
  </section>

  <section class="card card-back" aria-label="Business card back">
    <p class="mission">
      We help [target demographic]<br>
      achieve [desired emotional outcome]<br>
      by [our unique approach]<br>
      because [our brand beliefs]
    </p>
    <div class="back-watermark" aria-hidden="true">NORTHLARK</div>
  </section>
</main>
</body>
</html>
```